Lullio.com re-design on Wix platform

Re-do this website : www.lullio.com
Lullio is a sound conditioner that uses the calming, sedative qualities of mundane rhythmic stimulation to allow its users to rest easier and deeper than they normally would.
I think of Lullio.com as a web app; a place to use and buy the product. Im open to suggestion on site layouts, whether you use one page or several.
Use the same color scheme: purple, white, black, grey/silver
I would like a place for testimonials, even though you don't currently see one on the site. Other than that, assume the content will stay mostly the same.
I'd like a clean, modern, professional look. The site will reside on Wix platform.

```html
<!DOCTYPE html>
<html lang="en">
<head>
<meta charset="utf-8">
<title>Lullio – Sound for Deeper Sleep</title>
<link rel="stylesheet" href="https://fonts.googleapis.com/css2?family=Source+Sans+3:wght@400;600;700&display=swap">
<style>
  :root {
    --purple: #6633cc;
    --purple-soft: #9172cc;
    --white: #ffffff;
    --black: #111111;
    --grey: #9a9a9a;
    --grey-light: #c9c9c9;
    --field-border: #cfcfcf;
    --placeholder: #9a9a9a;
  }
  * { box-sizing: border-box; margin: 0; padding: 0; }
  html, body { width: 726px; height: 1200px; overflow: hidden; background: var(--white); }
  body { position: relative; font-family: "Source Sans 3", "Myriad Pro", sans-serif; color: var(--black); }

  .site-header { position: absolute; left: 0; top: 0; width: 726px; height: 50px; }
  .brand { position: absolute; left: 29px; top: 10px; font-size: 27px; font-weight: 600; color: var(--black); letter-spacing: 0.5px; line-height: 1; }
  .social { position: absolute; right: 28px; top: 23px; display: flex; gap: 14px; }
  .social span { width: 20px; height: 20px; border-radius: 50%; background: var(--grey-light); display: block; }

  .hero { position: absolute; left: 8px; top: 50px; width: 709px; height: 336px; overflow: hidden; }
  .hero-visual { position: absolute; inset: 0; background: linear-gradient(100deg, #d9d4d0 0%, #c9bdb4 30%, #bdb9b6 55%, #a5a4a6 80%, #9e9ea2 100%); }
  .hero-controls { position: absolute; inset: 0; }
  .benefits { position: absolute; left: 399px; top: 36px; color: var(--white); }
  .benefits h2 { font-size: 15px; font-weight: 700; letter-spacing: 0.1px; margin-bottom: 2px; }
  .benefits ul { list-style: none; margin-left: 75px; font-size: 8.6px; font-weight: 600; line-height: 11.35px; }

  .offer { position: absolute; left: 57px; top: 467px; width: 155px; }
  .download-btn { display: flex; align-items: center; height: 36px; width: 155px; background: var(--purple); border-radius: 3px; padding: 4px; }
  .download-btn .label { color: var(--white); font-size: 12px; font-weight: 700; width: 84px; text-align: center; letter-spacing: 0.2px; }
  .download-btn .price { background: var(--white); height: 28px; flex: 1; display: flex; align-items: center; justify-content: center; font-size: 14.5px; font-weight: 700; }
  .offer-text { position: absolute; left: -20px; width: 195px; top: 56px; text-align: center; font-size: 14.5px; font-weight: 700; line-height: 19px; }

  .community { position: absolute; left: 505px; top: 412px; width: 185px; text-align: center; }
  .community svg { display: block; margin: 0 auto; }
  .community p { font-size: 14.5px; font-weight: 700; line-height: 19px; margin-top: 5px; }

  .subscribe { position: absolute; left: 178px; top: 654px; width: 396px; height: 36px; background: var(--purple); border-radius: 3px; display: flex; align-items: center; padding: 4px 6px; }
  .subscribe .field { width: 259px; height: 28px; background: var(--white); display: flex; align-items: center; padding-left: 8px; font-size: 14.5px; font-weight: 600; color: var(--placeholder); }
  .subscribe .action { flex: 1; text-align: center; color: var(--white); font-size: 14.5px; font-weight: 700; }

  .contact-band { position: absolute; left: 8px; top: 763px; width: 708px; height: 377px; background: var(--purple); }
  .contact-form { position: absolute; left: 69px; top: 50px; width: 240px; color: var(--white); }
  .contact-form h3 { font-size: 17px; font-weight: 700; margin-bottom: 9px; }
  .contact-form label { display: block; font-size: 14px; font-weight: 700; line-height: 18px; }
  .contact-form .input { width: 231px; height: 40px; background: var(--white); border: 2px solid var(--field-border); border-radius: 3px; margin: 1px 0 4px 1px; }
  .contact-form .input.message { height: 123px; }

  .testimonial { position: absolute; left: 368px; top: 16px; width: 322px; height: 345px; background: var(--purple-soft); color: #ece6f8; text-align: center; }
  .testimonial .author { position: absolute; top: 120px; width: 100%; font-size: 14.5px; font-weight: 700; }
  .testimonial blockquote { position: absolute; top: 161px; left: 40px; width: 242px; font-size: 14.5px; font-weight: 700; line-height: 19px; }
  .testimonial svg { position: absolute; top: 170px; }

  .site-footer { position: absolute; left: 8px; top: 1140px; width: 708px; height: 60px; background: var(--grey); }
  .site-footer p { position: absolute; right: 22px; top: 25px; color: var(--white); font-size: 12px; font-weight: 700; letter-spacing: 0.2px; }
</style>
</head>
<body>
  <header class="site-header">
    <div class="brand">Lullio</div>
    <nav class="social" aria-label="Social links"><span></span><span></span><span></span></nav>
  </header>

  <section class="hero">
    <div class="hero-visual" role="img" aria-label="Photo of a woman sleeping peacefully on white pillows"></div>
    <svg class="hero-controls" width="709" height="336" viewBox="0 0 709 336">
      <circle cx="185" cy="179" r="70" fill="none" stroke="#cfcfcf" stroke-width="4"/>
      <polygon points="160,135 160,223 233,179" fill="#cfcfcf"/>
      <polygon points="22,179 45,166 45,192" fill="#cfcfcf"/>
      <polygon points="687,179 665,166 665,192" fill="#d8d8d8"/>
    </svg>
    <div class="benefits">
      <h2>PROVEN BENEFITS OF PLENTIFUL REST</h2>
      <ul>
        <li>Better moods</li><li>More focus</li><li>More energy</li><li>A longer life</li>
        <li>Better sex</li><li>Fewer dangerous mistakes</li><li>Less pain</li>
        <li>Fewer signs of aging</li><li>A stronger immune system</li>
        <li>Learning and remembering better</li><li>Fewer heart problems</li>
        <li>Better vision</li><li>Happiness</li><li>Building muscle more easily</li>
        <li>Speaking better</li><li>Less headaches and migraines</li><li>Healthier skin</li>
        <li>Driving safer</li><li>Smaller chance of developing diabetes</li>
        <li>Smaller chance of certain kinds of cancer</li><li>Spending less money on health care</li>
      </ul>
    </div>
  </section>

  <section class="offer">
    <div class="download-btn"><span class="label">DOWNLOAD</span><span class="price">$ 2.99</span></div>
    <p class="offer-text">Download 10 continues hour fore deep sleep</p>
  </section>

  <section class="community">
    <svg width="116" height="100" viewBox="0 0 116 100" aria-hidden="true">
      <g fill="#000">
        <circle cx="30" cy="20" r="17"/>
        <circle cx="86" cy="20" r="17"/>
        <path d="M0 75 C0 48 14 38 30 38 C46 38 60 48 60 75 Z"/>
        <path d="M56 75 C56 48 70 38 86 38 C102 38 116 48 116 75 Z"/>
        <circle cx="58" cy="38" r="20" stroke="#fff" stroke-width="4"/>
        <path d="M20 100 C20 70 38 58 58 58 C78 58 96 70 96 100 Z" stroke="#fff" stroke-width="4"/>
      </g>
    </svg>
    <p>see what our customer feel after they use our product</p>
  </section>

  <form class="subscribe">
    <div class="field">Email Address</div>
    <div class="action">subscribe now</div>
  </form>

  <section class="contact-band">
    <div class="contact-form">
      <h3>QUESTIONS OR COMMENTS?</h3>
      <label>Name</label><div class="input"></div>
      <label>Email</label><div class="input"></div>
      <label>Message</label><div class="input message"></div>
    </div>
    <div class="testimonial">
      <div class="author">Dana Morrell</div>
      <blockquote>this song or sound was make me enjoy my sleep and feel more betten whe wake up</blockquote>
      <svg style="left:6px" width="22" height="26" viewBox="0 0 22 26"><polygon points="0,13 22,0 22,26" fill="#cfcfcf"/></svg>
      <svg style="right:2px" width="22" height="26" viewBox="0 0 22 26"><polygon points="22,13 0,0 0,26" fill="#d8d8d8"/></svg>
    </div>
  </section>

  <footer class="site-footer">
    <p>© 2017 LULLIO. ALL RIGHTS RESERVED.</p>
  </footer>
</body>
</html>
```